Bridal Pastry Trade Institute Website Homepage Revision

I need the "homepage" to the new Coastal Bridal Pastry Trade Institute to reworked. The current homepage is dull. It needs the attention of a professional graphic artist so it delivers a professionally finished feel and look. I have included the current URL for your viewing (builds.vornelt.com/coastal-pastry/cms/ ) to see where we are in the development phase. The elements on the homepage are all necessary and the colors are correct. I have also included the original Word document for the page (you can extract the RGB values and images from the doc). To be clear, I am not looking to recreate all the web pages, just the homepage. It needs to be responsive and stretched.

Target Market(s)

All bakers who sell wedding cakes in the United States

Number of Pages Required

1 page

Font styles to use
Other font styles liked:
• see the Word Document

Requirements
Must have
• It must have the elements already in the original mock up. That includes the colors and fonts.

```html
<!DOCTYPE html>
<html lang="en">
<head>
<meta charset="utf-8">
<title>Coastal Bridal Pastry Trade Institute</title>
<link href="https://fonts.googleapis.com/css2?family=Roboto+Condensed:wght@400;700&family=Open+Sans:wght@400;600&display=swap" rel="stylesheet">
<style>
:root{
  --nav:#262626;
  --teal:#22b6b1;
  --orange:#f47b20;
  --grey-band:#cfcfcf;
  --logo-strip:#ececec;
  --badge:#b9b9b9;
  --slate:#cfdde0;
  --purple:#5b2d91;
  --magenta:#c1138c;
  --footer:#8b0e55;
  --footer-head:#f06fce;
  --ink:#333;
  --white:#fff;
}
*{box-sizing:border-box;margin:0;padding:0}
html,body{width:1200px;height:3536px;overflow:hidden}
body{font-family:"Open Sans",Arial,sans-serif;color:var(--ink);background:var(--white);position:relative}

/* nav */
.site-nav{height:66px;background:var(--nav);display:flex;justify-content:center;align-items:stretch;font-family:"Roboto Condensed",Arial,sans-serif}
.site-nav a{color:var(--white);text-decoration:none;font-size:17px;display:flex;align-items:center;padding:0 17px}
.site-nav a.active{background:var(--teal);padding:0 26px}

/* hero */
.hero{height:519px;background:linear-gradient(160deg,#6b4332 0%,#4e2f22 55%,#3a2219 100%);display:flex;align-items:center;justify-content:center;flex-direction:column}
.hero .brand-mark{width:90px;height:90px;border-radius:50%;background:#c58a5e;margin-bottom:28px}
.hero .brand-name{font-family:"Roboto Condensed",Arial,sans-serif;font-weight:700;font-size:58px;color:#d9a175;letter-spacing:1px;text-align:center;line-height:1.1;max-width:900px}

/* as seen on */
.press{height:105px;display:flex;background:var(--logo-strip)}
.press .label{width:217px;background:#000;color:var(--white);font-family:"Roboto Condensed",Arial,sans-serif;font-size:19px;display:flex;align-items:center;justify-content:center;text-align:center;line-height:1.3}
.press .badges{flex:1;display:flex;justify-content:space-around;align-items:center;padding:0 40px}
.press .badge{width:62px;height:40px;background:var(--badge);border-radius:6px}
.press .badge.round{width:46px;height:46px;border-radius:50%}
.press .badge.wide{width:90px;height:26px}

/* video */
.video-band{height:505px;background:var(--grey-band);position:relative}
.video{position:absolute;left:111px;top:67px;width:617px;height:356px;background:linear-gradient(90deg,#7d8a96 0%,#b8c2cc 45%,#eceff2 60%,#f6f6f6 100%);box-shadow:0 2px 8px rgba(0,0,0,.3)}
.video .quote{position:absolute;left:345px;top:62px;font-family:"Roboto Condensed",Arial,sans-serif;font-weight:700;font-size:30px;color:#8b1a1a}
.video .caption{position:absolute;left:372px;top:130px;width:220px;text-align:right;font-weight:700;font-size:19px;line-height:1.45;color:#222}
.video .play{position:absolute;left:280px;top:140px}
.optin{position:absolute;left:757px;top:69px;width:330px;height:354px;background:var(--teal);border:3px solid #e7f6f5;padding:18px 20px;box-shadow:0 2px 8px rgba(0,0,0,.25)}
.optin h2{font-family:"Roboto Condensed",Arial,sans-serif;font-weight:400;color:var(--white);font-size:24px;text-align:center;line-height:1.3;padding:0 18px 18px;border-bottom:1px solid rgba(255,255,255,.6);margin-bottom:24px}
.field{width:100%;height:48px;background:var(--white);border:0;font-size:15px;padding:0 14px;display:flex;align-items:center;color:#444;margin-bottom:18px}
.btn{background:var(--orange);color:var(--white);font-family:"Roboto Condensed",Arial,sans-serif;font-size:22px;display:flex;align-items:center;justify-content:center}
.optin .btn{height:42px}

/* paths */
.paths{height:342px;background:var(--teal);text-align:center;color:var(--white);padding-top:38px}
.paths h2{font-family:"Roboto Condensed",Arial,sans-serif;font-weight:400;font-size:26px;line-height:1.6}
.path-list{display:flex;justify-content:center;gap:30px;margin-top:30px}
.path{width:224px;height:121px;border:2px solid var(--white);position:relative;padding-top:20px;font-family:"Roboto Condensed",Arial,sans-serif;font-size:19px;line-height:1.55}
.path .click{position:absolute;left:50%;bottom:-10px;transform:translateX(-50%);background:var(--white);color:#111;font-size:14px;width:106px;height:28px;line-height:28px;border-radius:3px;font-family:"Open Sans",Arial,sans-serif}

/* features */
.features{height:514px;background:var(--white);position:relative}
.feature{position:absolute;top:92px;width:321px;height:332px}
.feature .photo{height:226px;box-shadow:0 2px 6px rgba(0,0,0,.25)}
.feature .card{position:absolute;left:17px;right:17px;top:186px;height:146px;background:var(--white);box-shadow:0 2px 8px rgba(0,0,0,.25);text-align:center;padding:18px 16px 0;font-size:13px;line-height:1.5}
.feature .more{width:80px;height:26px;margin:10px auto 0;font-size:14px;font-family:"Open Sans",Arial,sans-serif;border-radius:2px}

/* about */
.about{height:622px;background:var(--slate);position:relative}
.about .portrait{position:absolute;left:99px;top:82px;width:356px;height:465px;border:6px solid var(--white);background:linear-gradient(160deg,#b7a58f 0%,#e4d5c2 45%,#3b3b3b 100%);box-shadow:0 2px 8px rgba(0,0,0,.25);overflow:hidden}
.about .portrait .ribbon{position:absolute;right:-40px;top:22px;transform:rotate(45deg);background:#c43a55;color:var(--white);font-family:"Roboto Condensed",Arial,sans-serif;font-size:17px;width:170px;text-align:center;padding:4px 0}
.about .copy{position:absolute;left:493px;top:88px;width:620px}
.about h2{font-family:"Roboto Condensed",Arial,sans-serif;font-weight:400;color:var(--purple);font-size:29px;line-height:1.3;margin-bottom:18px}
.about p{font-size:14.5px;line-height:1.6;margin-bottom:14px}
.about h3{font-family:"Roboto Condensed",Arial,sans-serif;font-weight:400;color:#e06a1a;font-size:20px;margin:22px 0 12px}

/* join */
.join{height:377px;background:var(--teal);color:var(--white);text-align:center;padding-top:62px}
.join h2{font-family:"Roboto Condensed",Arial,sans-serif;font-weight:400;font-size:29px;line-height:1.32}
.join-form{display:flex;justify-content:center;gap:11px;margin-top:32px}
.join-form .field{width:366px;height:61px;margin:0}
.join-form .btn{width:200px;height:61px;font-size:26px}
.join .note{font-size:15px;margin-top:30px}

/* social */
.social{height:97px;background:var(--magenta);display:flex;justify-content:center;align-items:center;gap:9px}
.social span{width:37px;height:37px;border:2px solid var(--white);border-radius:50%}

/* footer */
.site-footer{height:394px;background:var(--footer);position:relative;color:var(--white)}
.foot-col{position:absolute;top:44px}
.foot-col h4{font-family:"Roboto Condensed",Arial,sans-serif;font-weight:400;color:var(--footer-head);font-size:21px;margin-bottom:14px}
.foot-col ul{list-style:none}
.foot-col li{font-size:14px;line-height:26px;padding-left:16px;position:relative}
.foot-col li::before{content:"";position:absolute;left:0;top:9px;border-left:6px solid var(--white);border-top:4px solid transparent;border-bottom:4px solid transparent}
.foot-col h4.sub{margin-top:26px}
.site-footer .rule{position:absolute;left:92px;right:92px;top:325px;border-top:1px solid rgba(255,255,255,.4)}
.site-footer .copy{position:absolute;left:0;right:0;top:348px;text-align:center;font-size:15px}
</style>
</head>
<body>

<nav class="site-nav">
  <a class="active" href="#">Home</a>
  <a href="#">Cal's Story</a>
  <a href="#">Marketing Solutions</a>
  <a href="#">Sales Solutions</a>
  <a href="#">Hire Us</a>
  <a href="#">Contact</a>
  <a href="#">Member Login</a>
  <a href="#">Partner With Us</a>
  <a href="#">Blog</a>
</nav>

<header class="hero" role="img" aria-label="Warm wooden wall backdrop with the institute name">
  <div class="brand-mark"></div>
  <div class="brand-name">Coastal Bridal Pastry Trade Institute</div>
</header>

<section class="press">
  <div class="label">CAL BRENNAN<br>AS SEEN ON</div>
  <div class="badges">
    <div class="badge"></div>
    <div class="badge"></div>
    <div class="badge wide"></div>
    <div class="badge round"></div>
    <div class="badge"></div>
    <div class="badge wide"></div>
    <div class="badge"></div>
  </div>
</section>

<section class="video-band">
  <div class="video" role="img" aria-label="Video still of the presenter speaking about bridal concerns">
    <div class="quote">"principle of fear"</div>
    <div class="caption">You are helping your bride overcome 3 of the top 15 concerns she has.</div>
    <svg class="play" width="60" height="60" viewBox="0 0 60 60"><circle cx="30" cy="30" r="28" fill="#f47b20"/><path d="M24 18 L42 30 L24 42 Z" fill="#fff"/></svg>
  </div>
  <div class="optin">
    <h2>How a New Discovery Sells More Wedding Cakes and at Higher Prices!</h2>
    <div class="field">Your Name</div>
    <div class="field">Your Email</div>
    <div class="btn">Watch Now</div>
  </div>
</section>

<section class="paths">
  <h2>Our research is not just a game changer. It is the game changer.<br>We're rewriting the book for selling wedding cakes</h2>
  <div class="path-list">
    <div class="path">I'm New to Selling<br>Wedding Cakes...<span class="click">Click Here</span></div>
    <div class="path">I Want to Maintain<br>My Sales...<span class="click">Click Here</span></div>
    <div class="path">I'm Eager to Boost My<br>Sales and Profits...<span class="click">Click Here</span></div>
    <div class="path">I'm Ready to Dominate<br>My Market Area...<span class="click">Click Here</span></div>
  </div>
</section>

<section class="features">
  <article class="feature" style="left:94px">
    <div class="photo" role="img" aria-label="Team of bakers in white uniforms holding an award book" style="background:linear-gradient(180deg,#3a3a3a,#8a8a8a 60%,#d8d8d8)"></div>
    <div class="card">Become the "a Town's Finest." You'll have an atmosphere so special, brides won't think of using anyone but you!<div class="btn more">Read More</div></div>
  </article>
  <article class="feature" style="left:441px">
    <div class="photo" role="img" aria-label="Puzzled woman beside a large question mark" style="background:linear-gradient(90deg,#2b2b2b,#5a4a44 45%,#3a3a3a)"></div>
    <div class="card">Peek at a very effective psychological-sales riddle called "The Doubt Divide."<div class="btn more">Read More</div></div>
  </article>
  <article class="feature" style="left:790px">
    <div class="photo" role="img" aria-label="Split portrait showing two contrasting sides" style="background:linear-gradient(90deg,#e9c9a8,#f1dcc7 50%,#cfcfcf 50%,#9a9a9a)"></div>
    <div class="card">Discover a sales growth secret that reveals the "Two Sides of Your Wedding Cake Business."<div class="btn more">Read More</div></div>
  </article>
</section>

<section class="about">
  <div class="portrait" role="img" aria-label="Portrait of founder Cal Brennan in a patterned jacket">
    <div class="ribbon">Cal Brennan</div>
  </div>
  <div class="copy">
    <h2>Use Cutting-edge Methods Proven to Generate MORE Leads, Convince MORE Brides to Choose You, Get HIGHER Prices and DOMINATE Your Competition.</h2>
    <p>Our breakthrough marketing and sales methods are possible due to the long-term research studies we've conducted with 150,000 brides over the past 12 years.</p>
    <p>From the findings, we have developed new and revolutionary marketing strategies, sales tools, and a complete transformational wedding cake sales system.</p>
    <p>But, don't take my word for it...let me "prove" the value and impact they will have on your wedding cake business.</p>
    <h3>Enter Your Name and Email Address Below.</h3>
    <p>Each month you'll receive our "Premier Bridal Pastry Marketing Letter." It's normally available for a $397 subscription fee. You'll receive the first year... absolutely FREE.</p>
  </div>
</section>

<section class="join">
  <h2>Join our "Inner Circle Letter" for FREE." You'll receive the latest research secrets<br>while learning how to use psychology for gaining a decisive advantage to<br>market and sell your wedding cakes.</h2>
  <div class="join-form">
    <div class="field">Your Name:</div>
    <div class="field">Email address:</div>
    <div class="btn">Click to join</div>
  </div>
  <p class="note">We dislike spam as much as you do. Therefore, we'll never sell, rent, or give away your email address.</p>
</section>

<div class="social"><span></span><span></span><span></span><span></span><span></span></div>

<footer class="site-footer">
  <div class="foot-col" style="left:101px">
    <h4>Marketing Solutions</h4>
    <ul><li>Unlocking the Bride's Mind Course</li><li>Individual Marketing Videos</li><li>Bundled Marketing Videos</li><li>Trusted Cake Artisan</li><li>Advertise For Free</li><li>Analyze Your Marketing</li><li>Priority Ladder Training</li></ul>
  </div>
  <div class="foot-col" style="left:420px">
    <h4>Sales Solutions</h4>
    <ul><li>Individual Sales Tools</li><li>Bundles Sales Presentations</li><li>Premier Member Bulletin</li><li>Write a Wedding Cake Book</li><li>Analyze Your Sales System</li></ul>
  </div>
  <div class="foot-col" style="left:714px">
    <h4>Hire Us</h4>
    <ul><li>Coaching</li><li>Consulting</li><li>Speaking</li><li>3-Day Workshops</li></ul>
    <h4 class="sub">Partner With Us</h4>
    <ul><li>Spread the Word</li></ul>
  </div>
  <div class="foot-col" style="left:931px">
    <h4>Recent Blog Posts</h4>
    <ul><li>Coaching</li><li>Consulting</li><li>Speaking</li><li>3-Day Workshops</li></ul>
  </div>
  <div class="rule"></div>
  <div class="copy">© 2019 Company Name &nbsp;All right reserved</div>
</footer>

</body>
</html>
```